8 x 8 Social Media Design - Tax, Accounting & Bookkeeping Service

Bright Ledger Advisory Group, Inc.

Tax, Accounting and Bookkeeping Services

“We provide our services, with you next mortgage in mind”

Special pricing available for all Mortgage Loan Customers!!

President / CEO Marcus Delaney

Primary service provider with over 27 years of experience

Call directly for more information: (555) 284-9037

Or email at: mdelaney@brightledgerhq.example

```html
<!DOCTYPE html>
<html lang="en">
<head>
<meta charset="UTF-8">
<title>Bright Ledger Advisory Group – Tax, Accounting &amp; Bookkeeping</title>
<link rel="stylesheet" href="https://fonts.googleapis.com/css2?family=Poppins:wght@400;500;600;700&display=swap">
<style>
  :root {
    --navy: #1c4585;
    --ink: #1d2330;
    --gold: #b8963f;
    --white: #ffffff;
    --paper: #f5f7fa;
    --blue-pale: #c9d8ea;
    --blue-soft: #9fbad9;
    --blue-mid: #6b93c4;
    --blue-deep: #3f6fab;
  }
  * { margin: 0; padding: 0; box-sizing: border-box; }
  html, body { width: 1200px; height: 1200px; overflow: hidden; }
  body { font-family: "Poppins", sans-serif; background: var(--paper); }

  .poster { position: relative; width: 1200px; height: 1200px; overflow: hidden; background: var(--paper); }

  .shapes { position: absolute; inset: 0; width: 1200px; height: 1200px; }

  .brand {
    position: absolute; left: 110px; top: 70px; width: 400px;
    text-align: center; color: var(--navy);
  }
  .brand-mark { width: 46px; height: 46px; border-radius: 50%; background: var(--navy); margin: 0 auto 18px; }
  .brand-name { font-size: 34px; font-weight: 700; line-height: 1.15; }
  .brand-tagline { font-size: 15px; font-weight: 700; margin-top: 12px; letter-spacing: .3px; }
  .brand-est { font-size: 15px; font-weight: 700; margin-top: 4px; letter-spacing: 1px; }

  .photo-couple {
    position: absolute; left: 600px; top: 0; width: 600px; height: 536px;
    background: linear-gradient(160deg, #f2f3f5 0%, #e4e6ea 45%, #b9bfc9 75%, #6e6f78 100%);
  }
  .photo-ceo {
    position: absolute; left: 0; top: 410px; width: 470px; height: 490px;
    background: linear-gradient(180deg, #4b4b52 0%, #2a2a30 45%, #15161b 100%);
  }

  .headline {
    position: absolute; right: 40px; top: 548px; text-align: right;
    color: var(--navy); font-size: 52px; font-weight: 700; line-height: 1.2;
  }
  .subhead {
    position: absolute; right: 40px; top: 690px;
    color: var(--navy); font-size: 29px; font-weight: 400;
  }
  .offer {
    position: absolute; left: 704px; top: 768px; width: 496px; height: 132px;
    background: var(--gold); color: var(--white);
    font-size: 33px; font-weight: 600; line-height: 1.3;
    text-align: right; padding: 18px 40px 0 0;
  }

  .experience {
    position: absolute; left: 120px; top: 940px;
    color: var(--navy); font-size: 29px; font-weight: 600;
  }
  .contacts { position: absolute; left: 120px; top: 1000px; list-style: none; }
  .contact {
    display: flex; align-items: center; height: 56px;
    color: var(--ink); font-size: 28px; font-weight: 400;
  }
  .contact svg { width: 40px; height: 40px; margin-right: 24px; fill: var(--navy); }
  .contact .label { font-weight: 700; margin-right: 8px; }
  .divider { display: inline-block; width: 2px; height: 32px; background: var(--gold); margin: 0 18px; }
</style>
</head>
<body>
<main class="poster">
  <svg class="shapes" viewBox="0 0 1200 1200" aria-hidden="true">
    <rect x="0" y="300" width="600" height="600" fill="var(--blue-pale)"/>
    <circle cx="120" cy="420" r="220" fill="var(--blue-soft)" opacity=".7"/>
    <rect x="300" y="300" width="300" height="300" fill="var(--blue-mid)" opacity=".55"/>
    <circle cx="520" cy="380" r="150" fill="var(--blue-deep)" opacity=".45"/>
    <polygon points="0,600 260,900 0,900" fill="var(--blue-deep)" opacity=".6"/>
    <polygon points="300,600 640,900 300,900" fill="var(--blue-soft)" opacity=".6"/>
    <rect x="0" y="900" width="1200" height="300" fill="var(--paper)"/>
    <circle cx="1120" cy="1180" r="220" fill="var(--blue-mid)" opacity=".8"/>
    <polygon points="1200,900 1200,1150 980,1150" fill="var(--blue-deep)" opacity=".7"/>
    <circle cx="1080" cy="1000" r="110" fill="var(--blue-pale)" opacity=".8"/>
  </svg>

  <header class="brand">
    <div class="brand-mark"></div>
    <div class="brand-name">Bright Ledger Advisory Group, Inc.</div>
    <div class="brand-tagline">PLAN TODAY, WE'LL HANDLE THE REST.</div>
    <div class="brand-est">EST. 1997</div>
  </header>

  <div class="photo-couple" role="img" aria-label="Photo of a couple reviewing financial papers with a calculator at a kitchen table"></div>
  <div class="photo-ceo" role="img" aria-label="Portrait of the President and CEO in a dark hat and jacket"></div>

  <h1 class="headline">Tax, Accounting &amp;<br>Bookkeeping Services</h1>
  <p class="subhead">With Your Next Mortgage In Mind</p>
  <p class="offer">Special Pricing for<br>Mortgage Customers</p>

  <p class="experience">Primary service provider with over 27 years of experience</p>
  <ul class="contacts">
    <li class="contact">
      <svg viewBox="0 0 24 24" aria-hidden="true"><circle cx="12" cy="6" r="4.5"/><path d="M3 22c0-5 4-8.5 9-8.5s9 3.5 9 8.5z"/></svg>
      President / CEO<span class="divider"></span>Marcus Delaney
    </li>
    <li class="contact">
      <svg viewBox="0 0 24 24" aria-hidden="true"><path d="M6.6 10.8a15.1 15.1 0 0 0 6.6 6.6l2.2-2.2c.3-.3.7-.4 1-.2 1.1.4 2.3.6 3.6.6.6 0 1 .4 1 1V20c0 .6-.4 1-1 1A17 17 0 0 1 3 4c0-.6.4-1 1-1h3.5c.6 0 1 .4 1 1 0 1.3.2 2.5.6 3.6.1.3 0 .7-.2 1z"/></svg>
      Call: (555) 284-9037
    </li>
    <li class="contact">
      <svg viewBox="0 0 24 24" aria-hidden="true"><path d="M2 5h20v14H2z M3.5 6.5 12 13l8.5-6.5" fill="none" stroke="var(--navy)" stroke-width="2"/></svg>
      <span class="label">Email:</span>mdelaney@brightledgerhq.example
    </li>
  </ul>
</main>
</body>
</html>
```